Business cards real estate company

We need a design for a business card. It is a company that specializes in real estate sales. There should be space for a photo of the respective employee as well as the website and telephone number on it. Design should be noble, innovative.

Contact Information for Business Card

Website, Name, Position, Telefonnummer

Requirements
Must have
• Photo, logo

```html
<!DOCTYPE html>
<html lang="en">
<head>
<meta charset="utf-8">
<title>Verdanest – Business Card</title>
<link rel="stylesheet" href="https://fonts.googleapis.com/css2?family=Lato:wght@400;700&family=Raleway:wght@400;500&display=swap">
<style>
  :root {
    --lime: #abd04a;
    --green: #58b45b;
    --photo-fill: #e2ecb4;
    --ink: #141414;
    --paper: #ffffff;
  }
  * { margin: 0; padding: 0; box-sizing: border-box; }
  html, body { width: 999px; height: 1200px; overflow: hidden; background: var(--paper); }
  .sheet { position: relative; width: 999px; height: 1200px; font-family: "Lato", sans-serif; color: var(--ink); }
  .card { position: absolute; left: 39px; width: 945px; background: var(--paper); overflow: hidden; }
  .card--front { top: 18px; height: 567px; }
  .card--back { top: 603px; height: 567px; }
  .band { position: absolute; left: 0; width: 945px; display: block; }
  .band--top { top: 0; height: 66px; }
  .band--bottom { bottom: 0; height: 63px; }

  .photo-frame { position: absolute; left: 0; top: 44px; width: 330px; height: 418px; }
  .photo-frame__shadow { position: absolute; left: 0; top: 0; width: 341px; height: 434px; background: var(--green); }
  .photo-frame__rule { position: absolute; left: 0; top: 438px; width: 316px; height: 16px; border: 3px solid var(--lime); border-left: none; border-top: none; }
  .photo { position: absolute; left: 0; top: 0; width: 329px; height: 418px; background: var(--photo-fill);
           display: flex; align-items: flex-start; justify-content: center; padding-top: 117px; }
  .photo__label { font-family: "Raleway", sans-serif; font-weight: 500; font-size: 35px; letter-spacing: 3px; line-height: 63px; text-align: center; }

  .brand-small { position: absolute; left: 471px; top: 97px; font-size: 34px; font-weight: 700; color: var(--green); line-height: 1; }
  .person__name { position: absolute; left: 472px; top: 184px; font-size: 61px; font-weight: 700; line-height: 1; letter-spacing: -0.5px; }
  .person__title { position: absolute; left: 474px; top: 252px; font-family: "Raleway", sans-serif; font-size: 19px; line-height: 1; letter-spacing: 2px; }
  .person__rule { position: absolute; left: 474px; top: 278px; width: 356px; height: 4px; background: var(--lime); }

  .contact { position: absolute; left: 481px; display: flex; align-items: center; gap: 15px; font-size: 23px; }
  .contact--phone { top: 347px; }
  .contact--web { top: 425px; font-size: 22px; }
  .contact__icon { width: 56px; height: 56px; flex: none; }

  .brand-large { position: absolute; left: 0; width: 945px; top: 185px; text-align: center; font-size: 128px; font-weight: 700; color: var(--green); line-height: 1; letter-spacing: -1px; }
  .tagline { position: absolute; left: 0; width: 945px; top: 336px; text-align: center; font-family: "Raleway", sans-serif; font-size: 36px; letter-spacing: 4px; }
  .back-web { position: absolute; left: 0; width: 945px; top: 440px; text-align: center; font-size: 22px; }
</style>
</head>
<body>
<main class="sheet">

  <section class="card card--front">
    <svg class="band band--top" viewBox="0 0 945 66" preserveAspectRatio="none" aria-hidden="true">
      <rect width="945" height="66" fill="var(--green)"/>
      <polygon points="0,0 374,0 406,66 0,66" fill="var(--lime)"/>
    </svg>

    <div class="photo-frame">
      <div class="photo-frame__rule"></div>
      <div class="photo-frame__shadow"></div>
      <div class="photo" role="img" aria-label="Portrait photo of the employee">
        <p class="photo__label">PHOTO OF<br>EMPLOYEE</p>
      </div>
    </div>

    <p class="brand-small">Verdanest</p>
    <h1 class="person__name">Jorin Vaskel</h1>
    <p class="person__title">POSITION TITLE</p>
    <div class="person__rule"></div>

    <p class="contact contact--phone">
      <svg class="contact__icon" viewBox="0 0 56 56" aria-hidden="true">
        <circle cx="28" cy="28" r="28" fill="var(--green)"/>
        <path d="M20 15c1.5-1 3-.5 3.8.8l2.4 4.2c.7 1.2.4 2.6-.6 3.4l-1.8 1.4c1.2 3 3.6 5.6 6.6 7l1.5-1.8c.8-1 2.2-1.2 3.4-.5l4.2 2.4c1.3.8 1.8 2.4.8 3.8l-1.5 2c-1.6 2-4.4 2.4-6.8 1.3-6.6-3-11.6-8.2-14.4-14.8-1-2.4-.4-5 1.6-6.6z" fill="#fff"/>
      </svg>
      <span>0123 45 6789</span>
    </p>
    <p class="contact contact--web">
      <svg class="contact__icon" viewBox="0 0 56 56" aria-hidden="true">
        <circle cx="28" cy="28" r="28" fill="var(--green)"/>
        <g fill="none" stroke="#fff" stroke-width="2.6">
          <circle cx="28" cy="28" r="14"/>
          <ellipse cx="28" cy="28" rx="6" ry="14"/>
          <line x1="14" y1="28" x2="42" y2="28"/>
          <line x1="16" y1="21" x2="40" y2="21"/>
          <line x1="16" y1="35" x2="40" y2="35"/>
        </g>
      </svg>
      <span>www.verdanest-homes.com</span>
    </p>

    <svg class="band band--bottom" viewBox="0 0 945 63" preserveAspectRatio="none" aria-hidden="true">
      <rect width="945" height="63" fill="var(--lime)"/>
      <polygon points="0,0 564,0 533,63 0,63" fill="var(--green)"/>
    </svg>
  </section>

  <section class="card card--back">
    <svg class="band band--top" viewBox="0 0 945 66" preserveAspectRatio="none" aria-hidden="true">
      <rect width="945" height="66" fill="var(--green)"/>
      <polygon points="0,0 374,0 406,66 0,66" fill="var(--lime)"/>
    </svg>

    <h2 class="brand-large">Verdanest</h2>
    <p class="tagline">REAL ESTATE COMPANY</p>
    <p class="back-web">www.verdanest-homes.com</p>

    <svg class="band band--bottom" viewBox="0 0 945 63" preserveAspectRatio="none" aria-hidden="true">
      <rect width="945" height="63" fill="var(--lime)"/>
      <polygon points="0,0 564,0 533,63 0,63" fill="var(--green)"/>
    </svg>
  </section>

</main>
</body>
</html>
```